Calder Ridge Minerals

Looking for a cool, glossy business card...white with our logo on one side and then the a smaller version of the logo on the other side (top left hand corner) and then the name and position of the person next to it, and then the office address and email address on the bottom left hand corner and the phone numbers & email address on the bottom right hand corner. I have the logo already...can pass it on when you're ready.

```html
<!DOCTYPE html>
<html lang="en">
<head>
<meta charset="utf-8">
<title>Calder Ridge Minerals – Business Card</title>
<link href="https://fonts.googleapis.com/css2?family=Cinzel:wght@400&family=Merriweather:wght@300;400&display=swap" rel="stylesheet">
<style>
  :root {
    --backdrop: #2c2c2e;
    --card: #18181a;
    --ink: #f2f2f2;
    --ink-soft: #cfcfcf;
    --accent-blue: #1f2fd6;
    --accent-red: #c0141c;
  }
  * { margin: 0; padding: 0; box-sizing: border-box; }
  html, body {
    width: 799px; height: 1200px; overflow: hidden;
    background: var(--backdrop);
  }
  .canvas {
    position: relative; width: 799px; height: 1200px;
  }
  .card {
    position: absolute; left: 70px; width: 660px; height: 380px;
    background: var(--card);
    border-radius: 6px;
    box-shadow: 0 14px 30px rgba(0,0,0,.45);
  }
  .card--front { top: 100px; }
  .card--back { top: 710px; }

  .wordmark {
    font-family: "Cinzel", serif;
    font-weight: 400;
    color: var(--ink);
    letter-spacing: 1px;
    white-space: nowrap;
    display: flex; align-items: center; gap: 12px;
  }
  .wordmark__dot {
    width: 12px; height: 12px; border-radius: 50%;
    background: var(--ink);
  }
  .card--front .wordmark {
    position: absolute; left: 0; right: 0; top: 170px;
    justify-content: center; font-size: 36px;
  }
  .card--back .wordmark {
    position: absolute; right: 40px; top: 120px; font-size: 24px;
  }

  .person {
    position: absolute; left: 40px; top: 50px;
    font-family: "Merriweather", serif;
  }
  .person__name {
    font-variant: small-caps; font-size: 20px; color: var(--accent-blue);
    letter-spacing: 1px;
  }
  .person__role { font-size: 13px; color: var(--ink-soft); margin-top: 4px; font-weight: 300; }
  .person__address {
    font-size: 13px; color: var(--ink-soft); margin-top: 26px; line-height: 1.5; font-weight: 300;
  }
  .divider {
    position: absolute; left: 210px; right: 40px; top: 185px;
    height: 2px; background: var(--accent-blue);
  }
  .contact {
    position: absolute; right: 40px; bottom: 60px;
    font-family: "Merriweather", serif; font-weight: 300;
    font-size: 15px; color: var(--ink-soft); list-style: none;
  }
  .contact__item {
    display: flex; align-items: center; justify-content: flex-end; gap: 12px;
    line-height: 28px;
  }
  .contact__icon { width: 14px; height: 14px; flex: none; }
</style>
</head>
<body>
<main class="canvas">
  <section class="card card--front" aria-label="Card front">
    <div class="wordmark"><span class="wordmark__dot"></span>Calder Ridge Minerals</div>
  </section>

  <section class="card card--back" aria-label="Card back">
    <div class="person">
      <p class="person__name">Dale R Hutchins</p>
      <p class="person__role">Managing Director</p>
      <p class="person__address">4120 Ranch Rd #210<br>Del Rio, TX 78840</p>
    </div>
    <div class="wordmark"><span class="wordmark__dot"></span>Calder Ridge Minerals</div>
    <div class="divider"></div>
    <ul class="contact">
      <li class="contact__item">(830) 555-0147
        <svg class="contact__icon" viewBox="0 0 14 14" aria-hidden="true"><circle cx="7" cy="7" r="7" fill="var(--accent-red)"/><path d="M4.5 3.5 l1.5 0 l.6 1.8 -.9 .7 a5 5 0 0 0 2.3 2.3 l.7-.9 1.8.6 0 1.5 a1 1 0 0 1-1 1 A6 6 0 0 1 3.5 4.5 a1 1 0 0 1 1-1z" fill="#18181a"/></svg>
      </li>
      <li class="contact__item">info@calderridgeminerals.com
        <svg class="contact__icon" viewBox="0 0 14 14" aria-hidden="true"><circle cx="7" cy="7" r="7" fill="var(--accent-red)"/><rect x="3.5" y="4.5" width="7" height="5" fill="none" stroke="#18181a" stroke-width="1"/><path d="M3.5 4.5 L7 7.3 L10.5 4.5" fill="none" stroke="#18181a" stroke-width="1"/></svg>
      </li>
      <li class="contact__item">www.calderridgeminerals.com
        <svg class="contact__icon" viewBox="0 0 14 14" aria-hidden="true"><circle cx="7" cy="7" r="7" fill="var(--accent-red)"/><circle cx="7" cy="7" r="3.6" fill="none" stroke="#18181a" stroke-width="1"/><path d="M3.4 7h7.2M7 3.4c-1.6 2-1.6 5.2 0 7.2M7 3.4c1.6 2 1.6 5.2 0 7.2" fill="none" stroke="#18181a" stroke-width=".9"/></svg>
      </li>
    </ul>
  </section>
</main>
</body>
</html>
```